Computer Training in the Education sector - Letterhead

We need a new letter head to be designed for the company. We provide computer training fro the Education Sector, both primary and private tertiary providers. The colours will need to tie in with the website www.lanternpathlearning.co.nz.
The company name is Lantern Path Co with the tag line of Computer Training for Educators.
The footer will need to have the following detail...
0508 KEY MENTOR
027 813 459
www.lanternpathlearning.co.nz / lessons@lanternpathlearning.co.nz
Updates

Thanks for the designs so far.

Some have watermarks in the background. Please don't worry about using watermarks as I will not be using a watermark in in a final design.
Regards,
Morris

Thank you for all the designs and the effort. There was some great concepts that came through.

Cheers
Morris

Industry/Entity Type

Computer

```html
<!DOCTYPE html>
<html lang="en">
<head>
<meta charset="utf-8">
<title>Lantern Path Co – Letterhead and Business Card</title>
<link rel="stylesheet" href="https://fonts.googleapis.com/css2?family=Arimo:wght@400;700&family=Varela+Round&display=swap">
<style>
  :root {
    --stage: #c9c8f7;
    --stage-light: #e4e3fc;
    --paper: #ffffff;
    --brand-blue: #5b8def;
    --band-blue: #6666f2;
    --brand-green: #1fc31f;
    --brand-orange: #f7941d;
    --ink: #111111;
    --on-band: #ffffff;
  }
  * { box-sizing: border-box; margin: 0; padding: 0; }
  html, body { width: 1200px; height: 1000px; overflow: hidden; }
  body {
    background: radial-gradient(circle at 60% 45%, var(--stage-light), var(--stage) 75%);
    font-family: "Varela Round", Arial, sans-serif;
    position: relative;
  }

  /* ---------- Letterhead ---------- */
  .letterhead {
    position: absolute; left: 110px; top: 90px;
    width: 560px; height: 800px;
    background: var(--paper);
    box-shadow: 0 4px 14px rgba(40, 40, 110, .35);
    overflow: hidden;
  }
  .letterhead__waves-top { position: absolute; left: 0; top: 0; width: 560px; height: 150px; }
  .letterhead__waves-bottom { position: absolute; left: 0; bottom: 0; width: 560px; height: 210px; }

  .brand { position: absolute; display: flex; align-items: center; }
  .brand__dot { border-radius: 50%; background: var(--brand-blue); flex: none; }
  .brand__name {
    font-family: "Arimo", Arial, sans-serif; font-weight: 700;
    color: var(--brand-blue); white-space: nowrap;
  }
  .brand__tagline {
    font-family: "Varela Round", Arial, sans-serif; color: var(--ink);
    border-top: 1.5px solid var(--ink); white-space: nowrap;
  }

  .letterhead .brand { left: 34px; top: 150px; gap: 18px; }
  .letterhead .brand__dot { width: 62px; height: 62px; }
  .letterhead .brand__name { font-size: 38px; line-height: 1; }
  .letterhead .brand__tagline {
    font-size: 13px; margin-top: 6px; padding-top: 2px;
    margin-left: 110px; border-top: none;
  }

  .date-field {
    position: absolute; right: 34px; top: 232px;
    font-family: "Arimo", Arial, sans-serif; font-weight: 700; font-size: 14px; color: var(--ink);
    display: flex; align-items: flex-end; gap: 6px;
  }
  .date-field__line { width: 150px; border-bottom: 1.5px solid var(--ink); height: 14px; }
  .letterhead__rule {
    position: absolute; left: 0; right: 0; top: 270px; border-top: 2px solid var(--ink);
  }

  .contact { position: absolute; color: var(--on-band); font-size: 13px; }
  .contact__row { display: flex; align-items: center; gap: 12px; height: 22px; white-space: nowrap; }
  .contact__icon { width: 15px; height: 15px; flex: none; }
  .contact__hash { width: 15px; text-align: center; font-size: 14px; flex: none; }

  .letterhead .contact--left { left: 34px; bottom: 22px; }
  .letterhead .contact--right { right: 30px; bottom: 40px; font-size: 14px; }

  /* ---------- Business card ---------- */
  .business-card {
    position: absolute; left: 730px; top: 370px;
    width: 380px; height: 220px;
    background: var(--paper);
    box-shadow: 0 4px 14px rgba(40, 40, 110, .35);
    overflow: hidden;
  }
  .business-card__waves { position: absolute; left: 0; bottom: 0; width: 380px; height: 110px; }
  .business-card .brand { left: 20px; top: 22px; gap: 14px; align-items: flex-start; }
  .business-card .brand__dot { width: 70px; height: 70px; }
  .business-card .brand__text { padding-top: 10px; }
  .business-card .brand__name { font-size: 22px; }
  .business-card .brand__tagline { font-size: 9px; margin-top: 6px; padding-top: 2px; padding-left: 10px; }
  .cardholder { position: absolute; right: 72px; top: 88px; text-align: center; }
  .cardholder__name {
    font-family: "Arimo", Arial, sans-serif; font-weight: 700; font-size: 13px; color: var(--brand-blue);
  }
  .cardholder__name-accent { color: var(--brand-orange); }
  .cardholder__role { font-family: "Arimo", Arial, sans-serif; font-size: 10px; color: var(--ink); }
  .business-card .contact { font-size: 9px; }
  .business-card .contact__row { height: 16px; gap: 8px; }
  .business-card .contact__icon { width: 11px; height: 11px; }
  .business-card .contact__hash { width: 11px; font-size: 10px; }
  .business-card .contact--left { left: 14px; bottom: 8px; }
  .business-card .contact--right { right: 14px; bottom: 8px; }
</style>
</head>
<body>

<svg width="0" height="0" style="position:absolute" aria-hidden="true">
  <defs>
    <symbol id="icon-mobile" viewBox="0 0 16 16">
      <circle cx="8" cy="8" r="7" fill="none" stroke="currentColor" stroke-width="1.4"/>
      <rect x="5.5" y="3.5" width="5" height="9" rx="1" fill="currentColor"/>
    </symbol>
    <symbol id="icon-phone" viewBox="0 0 16 16">
      <path d="M1 6c0-2 3-3.5 7-3.5S15 4 15 6l-3 1-1-2H5L4 7z" fill="currentColor"/>
      <path d="M4 8h8l1.5 6h-11z" fill="currentColor"/>
    </symbol>
    <symbol id="icon-home" viewBox="0 0 16 16">
      <path d="M1 8 8 2l7 6" fill="none" stroke="currentColor" stroke-width="1.6"/>
      <rect x="3.5" y="8" width="9" height="7" fill="currentColor"/>
    </symbol>
    <symbol id="icon-mail" viewBox="0 0 16 16">
      <rect x="1" y="3" width="14" height="10" fill="none" stroke="currentColor" stroke-width="1.4"/>
      <path d="M1 3.5 8 9l7-5.5" fill="none" stroke="currentColor" stroke-width="1.4"/>
    </symbol>
  </defs>
</svg>

<section class="letterhead" aria-label="Letterhead">
  <svg class="letterhead__waves-top" viewBox="0 0 560 150" preserveAspectRatio="none" aria-hidden="true">
    <path d="M0 0H560V62C420 70 220 90 0 146Z" fill="var(--brand-orange)"/>
    <path d="M0 0H560V52C420 58 220 76 0 128Z" fill="var(--brand-green)"/>
    <path d="M0 0H560V40C420 44 220 60 0 110Z" fill="var(--brand-blue)"/>
  </svg>

  <div class="brand">
    <span class="brand__dot"></span>
    <div class="brand__text">
      <div class="brand__name">Lantern Path Co</div>
      <div class="brand__tagline">... Computer Training for Educators</div>
    </div>
  </div>

  <div class="date-field"><span>Date:</span><span class="date-field__line"></span></div>
  <div class="letterhead__rule"></div>

  <svg class="letterhead__waves-bottom" viewBox="0 0 560 210" preserveAspectRatio="none" aria-hidden="true">
    <path d="M0 88C200 70 420 24 560 0V210H0Z" fill="var(--brand-orange)"/>
    <path d="M0 98C200 80 420 38 560 18V210H0Z" fill="var(--brand-green)"/>
    <path d="M0 108C200 92 420 54 560 36V210H0Z" fill="var(--band-blue)"/>
  </svg>

  <div class="contact contact--left">
    <div class="contact__row"><svg class="contact__icon"><use href="#icon-mobile"/></svg>027 813 459</div>
    <div class="contact__row"><svg class="contact__icon"><use href="#icon-phone"/></svg>0508 KEY MENTOR</div>
    <div class="contact__row"><span class="contact__hash">#</span>14 Kowhai Lane, Fernbrook, 4820</div>
  </div>
  <div class="contact contact--right">
    <div class="contact__row"><svg class="contact__icon"><use href="#icon-home"/></svg>www.lanternpathlearning.co.nz</div>
    <div class="contact__row"><svg class="contact__icon"><use href="#icon-mail"/></svg>lessons@lanternpathlearning.co.nz</div>
  </div>
</section>

<section class="business-card" aria-label="Business card">
  <div class="brand">
    <span class="brand__dot"></span>
    <div class="brand__text">
      <div class="brand__name">Lantern Path Co</div>
      <div class="brand__tagline">... Computer Training for Educators</div>
    </div>
  </div>

  <div class="cardholder">
    <div class="cardholder__name">Mr. <span class="cardholder__name-accent">Manager</span></div>
    <div class="cardholder__role">CEO</div>
  </div>

  <svg class="business-card__waves" viewBox="0 0 380 110" preserveAspectRatio="none" aria-hidden="true">
    <path d="M0 28C120 32 260 6 380 0V110H0Z" fill="var(--brand-orange)"/>
    <path d="M0 34C120 38 260 14 380 10V110H0Z" fill="var(--brand-green)"/>
    <path d="M0 42C120 46 260 24 380 20V110H0Z" fill="var(--band-blue)"/>
  </svg>

  <div class="contact contact--left">
    <div class="contact__row"><svg class="contact__icon"><use href="#icon-mobile"/></svg>027 813 459</div>
    <div class="contact__row"><svg class="contact__icon"><use href="#icon-phone"/></svg>0508 KEY MENTOR</div>
    <div class="contact__row"><span class="contact__hash">#</span>14 Kowhai Lane, Fernbrook, 4820</div>
  </div>
  <div class="contact contact--right">
    <div class="contact__row"><svg class="contact__icon"><use href="#icon-home"/></svg>www.lanternpathlearning.co.nz</div>
    <div class="contact__row"><svg class="contact__icon"><use href="#icon-mail"/></svg>lessons@lanternpathlearning.co.nz</div>
  </div>
</section>

</body>
</html>
```